Need a flyer overhaul and minor changes

flyer is 5.5" x 8.5" we need to change the $250.00 to $325.00, update our company logo on the brochure, and also have an area where we can have the store address (318 W Harlan Ave, Del Rio, TX 78840 - (830) 642-9158). I've attached a our current brochure and our updated logo and we just want to make look better and updated.

Industry/Entity Type

Lending and Finance

Requirements
Nice to have
• updated layout and pictures

```html
<!DOCTYPE html>
<html lang="en">
<head>
<meta charset="utf-8">
<title>Stuck in a Title Loan? Flyer</title>
<link href="https://fonts.googleapis.com/css2?family=Montserrat:wght@400;500;600;700;800&display=swap" rel="stylesheet">
<style>
  :root {
    --red: #c41e2b;
    --green: #1c6336;
    --ink: #111111;
    --paper: #ffffff;
    --row: #ececec;
    --band: #eeeeee;
    --stage: #e4e4e4;
    --frame: #555555;
    --photo-a: #e9ecef;
    --photo-b: #c9d6e2;
  }
  * { margin: 0; padding: 0; box-sizing: border-box; }
  html, body { width: 1200px; height: 605px; overflow: hidden; }
  body {
    background: var(--stage);
    font-family: "Montserrat", Arial, sans-serif;
    color: var(--ink);
  }
  .flyer {
    position: absolute;
    left: 395px; top: 12px;
    width: 410px; height: 580px;
    background: var(--paper);
    overflow: hidden;
    box-shadow: 0 4px 14px rgba(0,0,0,.25);
  }
  .header-shape { position: absolute; left: 0; top: 0; width: 410px; height: 140px; }
  .headline {
    position: absolute; left: 0; top: 14px; width: 410px;
    text-align: center; color: var(--paper); line-height: 1;
  }
  .headline .kicker { display: block; font-weight: 400; font-size: 34px; letter-spacing: .5px; }
  .headline .main { display: block; font-weight: 800; font-size: 49px; margin-top: 3px; letter-spacing: -.5px; }
  .comparison-pill {
    position: absolute; left: 32px; top: 103px; width: 346px; height: 28px;
    background: var(--green); color: var(--paper);
    border-radius: 14px 14px 14px 14px / 14px 14px 14px 14px;
    font-weight: 700; font-size: 19px; text-align: center; line-height: 28px;
  }
  .photo {
    position: absolute; left: 0; top: 134px; width: 200px; height: 356px;
    background: linear-gradient(160deg, var(--photo-a), var(--photo-b));
  }
  .table {
    position: absolute; left: 180px; top: 143px; width: 208px; height: 294px;
    background: var(--paper);
    border: 1.5px solid var(--frame); border-bottom: none;
    border-radius: 12px 12px 0 0;
  }
  .table .divider { position: absolute; left: 111px; top: 0; bottom: 0; width: 1.5px; background: var(--frame); }
  .col-head { position: absolute; top: 0; height: 52px; display: flex; align-items: center; justify-content: center; text-align: center; color: var(--green); }
  .col-head.ours { left: 0; width: 111px; font-weight: 700; font-size: 14px; }
  .col-head.title { left: 112px; width: 95px; font-weight: 800; font-size: 17px; line-height: .95; }
  .rows { position: absolute; left: 0; top: 52px; width: 206px; list-style: none; }
  .rows li { position: relative; height: 20px; font-weight: 700; font-size: 11.5px; line-height: 20px; }
  .rows li:nth-child(odd) { background: var(--row); }
  .rows .n { position: absolute; left: 18px; width: 22px; text-align: center; font-weight: 500; }
  .rows .ours { position: absolute; left: 46px; }
  .rows .title { position: absolute; left: 130px; }
  .result { position: absolute; color: var(--paper); font-weight: 800; text-align: center; line-height: .95; display: flex; flex-direction: column; justify-content: center; }
  .result.paid { left: 180px; top: 437px; width: 112px; height: 54px; background: var(--green); border-radius: 0 0 0 12px; font-size: 19px; }
  .result.owe { left: 291px; top: 437px; width: 97px; height: 54px; background: var(--red); border-radius: 0 0 12px 12px; font-size: 13px; }
  .result.owe strong { font-size: 18px; margin-top: 2px; }
  .footer-band { position: absolute; left: 0; top: 490px; width: 410px; height: 90px; background: var(--band); }
  .spanish-bar {
    position: absolute; left: 175px; top: 493px; width: 235px; height: 19px;
    background: var(--red); color: var(--paper);
    border-radius: 9px 0 0 9px;
    font-weight: 700; font-size: 13px; line-height: 19px; padding-left: 12px;
  }
  .brand-name {
    position: absolute; left: 18px; top: 512px; width: 140px;
    color: var(--green); font-weight: 700; font-size: 20px; line-height: 1.05;
  }
  .contact { position: absolute; left: 188px; top: 515px; width: 220px; }
  .contact .phone { display: flex; align-items: center; gap: 4px; font-weight: 600; font-size: 23px; line-height: 26px; }
  .contact .line { display: flex; align-items: center; gap: 6px; font-weight: 600; font-size: 10px; line-height: 14px; margin-left: 2px; }
  .contact .line em { font-style: normal; font-weight: 700; }
  .contact .line em span { color: var(--red); }
  .icon { flex: none; }
</style>
</head>
<body>
  <main class="flyer">
    <svg class="header-shape" viewBox="0 0 410 140" aria-hidden="true">
      <path d="M0 0H410V86Q205 104 0 86Z" fill="var(--red)"/>
      <path d="M0 86Q205 104 410 86V92Q205 112 0 92Z" fill="var(--green)"/>
    </svg>
    <h1 class="headline">
      <span class="kicker">STUCK IN A</span>
      <span class="main">TITLE LOAN?</span>
    </h1>
    <div class="comparison-pill">$1,000 LOAN COMPARISON</div>

    <div class="photo" role="img" aria-label="Photo of a smiling woman counting a stack of cash"></div>

    <section class="table">
      <div class="divider"></div>
      <div class="col-head ours">Keystone</div>
      <div class="col-head title">TITLE<br>LOAN</div>
      <ol class="rows">
        <li><span class="n">1</span><span class="ours">$131.67</span><span class="title">$325.00</span></li>
        <li><span class="n">2</span><span class="ours">$131.67</span><span class="title">$325.00</span></li>
        <li><span class="n">3</span><span class="ours">$131.67</span><span class="title">$325.00</span></li>
        <li><span class="n">4</span><span class="ours">$131.67</span><span class="title">$325.00</span></li>
        <li><span class="n">5</span><span class="ours">$131.67</span><span class="title">$325.00</span></li>
        <li><span class="n">6</span><span class="ours">$131.67</span><span class="title">$325.00</span></li>
        <li><span class="n">7</span><span class="ours">$131.67</span><span class="title">$325.00</span></li>
        <li><span class="n">8</span><span class="ours">$131.67</span><span class="title">$325.00</span></li>
        <li><span class="n">9</span><span class="ours">$131.67</span><span class="title">$325.00</span></li>
        <li><span class="n">10</span><span class="ours">$131.67</span><span class="title">$325.00</span></li>
        <li><span class="n">11</span><span class="ours">$131.67</span><span class="title">$325.00</span></li>
        <li><span class="n">12</span><span class="ours">$131.67</span><span class="title">$325.00</span></li>
      </ol>
    </section>

    <div class="footer-band"></div>
    <div class="result paid">PAID<br>OFF</div>
    <div class="result owe">STILL OWE<strong>$1,000</strong></div>

    <div class="spanish-bar">SE HABLA ESPAÑOL</div>
    <div class="brand-name">Keystone<br>Lending</div>

    <address class="contact">
      <div class="phone">
        <svg class="icon" width="14" height="16" viewBox="0 0 24 24" aria-hidden="true"><path d="M6.6 2.5c.6-.3 1.3 0 1.6.6l1.7 3.6c.3.6.1 1.2-.4 1.6l-1.6 1.2c.9 2.3 2.5 4.3 4.6 5.6l1.4-1.4c.5-.5 1.2-.5 1.7-.2l3.3 2.2c.5.4.7 1.1.3 1.7l-1.3 2c-.6.9-1.7 1.3-2.7.9C8.6 18.3 4.9 13.3 4 6.7c-.1-1 .4-2 1.3-2.6z" fill="var(--ink)"/></svg>
        (830) 642-9158
      </div>
      <div class="line">
        <svg class="icon" width="9" height="11" viewBox="0 0 24 30" aria-hidden="true"><path d="M12 0C5.4 0 0 5.2 0 11.6 0 20 12 30 12 30s12-10 12-18.4C24 5.2 18.6 0 12 0zm0 16a4.5 4.5 0 110-9 4.5 4.5 0 010 9z" fill="var(--ink)"/></svg>
        318 W Harlan Ave, Del Rio, TX 78840
      </div>
      <div class="line">
        <svg class="icon" width="10" height="10" viewBox="0 0 24 24" aria-hidden="true"><g fill="none" stroke="var(--ink)" stroke-width="2"><circle cx="12" cy="12" r="10"/><ellipse cx="12" cy="12" rx="4.5" ry="10"/><path d="M2 12h20M4 6.5h16M4 17.5h16"/></g></svg>
        <span>Visit us at <em>www.<span>keystonelending</span>.com</em></span>
      </div>
    </address>
  </main>
</body>
</html>
```